Business Card Design for Pastor/Church Leadership - simple, elegant, "different"

Design a name card based on logo and color from our branding guide - see file "MBF Logo and Color".
The teal frame around the logo is not part of the logo and is a not necessary design element for the name card (as the attached PDF file may suggest).
The font suggested by branding is "Frutiger 55 Roman".
The file "not good.pdf", a sample of a name card that is NOT good.
- fonts too small to read
- the tagline on the logo "Still waters, open door" not easy to read with logo used in this design
- "MAPLE GROVE FELLOWSHIP" unnecessarily duplicated - possibly because logo too small
- not sure about the green frame, probably better to drop

Target Market(s)

broad, all people the pastor of an international church in Tokyo meets

Industry/Entity Type

Business

Contact Information for Business Card

Mattias R. Pellworth
Pastor
3-9-4 Kawaranodai, Kaedeno-ku
Tokyo 162-0847 (Church)
2-21 Ochibamachi, Kaedeno-ku
Tokyo 162-0893 (Home)
Tel: 03-5817-2963
E-mail: pastor@maplegrovefell.org
URL: http://www.maplegrovefell.org

Font styles to use
Sans Serif
Other font styles liked:
• Frutiger 55 Roman (want, not must)

Requirements
Must have
• must include logo
• must make use of the "bright turquoise color"
• Cyan = 59, Magenta = 0, Yellow=24, Black=0
• Red=3.1%, Green=91%, Blue=87.1%
• Key Info (name) must be easy to read (see notes on bad sample namecard attached)

```html
<!DOCTYPE html>
<html lang="en">
<head>
<meta charset="utf-8">
<title>Mattias R. Pellworth, Pastor · Maple Grove Fellowship</title>
<link rel="stylesheet" href="https://fonts.googleapis.com/css2?family=Hind:wght@400&display=swap">
<style>
  :root {
    --teal: #5fc4c6;
    --turquoise: #6bffc4;
    --font: "Hind", "Frutiger", sans-serif;
  }
  html, body {
    margin: 0;
    padding: 0;
    overflow: hidden;
    background: var(--teal);
  }
  .card {
    position: relative;
    width: 1200px;
    height: 685px;
    overflow: hidden;
    background: var(--teal);
    font-family: var(--font);
    font-weight: 400;
    color: var(--turquoise);
  }
  .card__curves {
    position: absolute;
    inset: 0;
  }
  .brand {
    position: absolute;
    top: 36px;
    left: 0;
    width: 1200px;
    display: flex;
    flex-direction: column;
    align-items: center;
    color: var(--teal);
  }
  .brand__mark {
    width: 84px;
    height: 84px;
    border-radius: 50%;
    background: var(--teal);
    margin-bottom: 38px;
  }
  .brand__name {
    font-size: 16px;
    letter-spacing: 0.14em;
    line-height: 1;
    padding-bottom: 10px;
    border-bottom: 1.5px solid var(--teal);
  }
  .brand__tagline {
    font-size: 15px;
    line-height: 1;
    margin-top: 14px;
  }
  .person {
    position: absolute;
    top: 250px;
    left: 0;
    width: 1200px;
    text-align: center;
  }
  .person__name {
    font-size: 57px;
    font-weight: 400;
    line-height: 1;
    letter-spacing: 0.01em;
    margin: 0;
  }
  .person__role {
    font-size: 36px;
    line-height: 1;
    margin-top: 12px;
  }
  .envelope {
    position: absolute;
    top: 335px;
    width: 58px;
    height: 38px;
  }
  .envelope--church { left: 275px; }
  .envelope--home { left: 836px; }
  .address {
    position: absolute;
    top: 382px;
    font-size: 32px;
    line-height: 42px;
    margin: 0;
    font-style: normal;
  }
  .address--church { left: 87px; text-align: left; }
  .address--home { right: 84px; text-align: right; }
  .contact {
    position: absolute;
    top: 518px;
    left: 0;
    width: 1200px;
    display: flex;
    flex-direction: column;
    align-items: center;
    color: var(--teal);
    font-size: 32px;
    line-height: 45px;
  }
  .contact__line {
    display: flex;
    align-items: center;
    gap: 14px;
  }
  .contact__icon {
    width: 24px;
    height: 34px;
  }
  .contact__icon--at {
    width: 30px;
    height: 30px;
  }
</style>
</head>
<body>
<div class="card">
  <svg class="card__curves" width="1200" height="685" viewBox="0 0 1200 685" aria-hidden="true">
    <ellipse cx="600" cy="-105" rx="675" ry="330" fill="var(--turquoise)"/>
    <ellipse cx="600" cy="826" rx="724" ry="330" fill="var(--turquoise)"/>
  </svg>

  <div class="brand">
    <div class="brand__mark"></div>
    <div class="brand__name">MAPLE GROVE FELLOWSHIP</div>
    <div class="brand__tagline">Still waters, open door</div>
  </div>

  <div class="person">
    <h1 class="person__name">MATTIAS R. PELLWORTH</h1>
    <div class="person__role">Pastor</div>
  </div>

  <svg class="envelope envelope--church" viewBox="0 0 58 38" aria-hidden="true">
    <rect width="58" height="38" rx="2" fill="var(--turquoise)"/>
    <path d="M2 3 L29 22 L56 3" fill="none" stroke="var(--teal)" stroke-width="2.5"/>
  </svg>
  <svg class="envelope envelope--home" viewBox="0 0 58 38" aria-hidden="true">
    <rect width="58" height="38" rx="2" fill="var(--turquoise)"/>
    <path d="M2 3 L29 22 L56 3" fill="none" stroke="var(--teal)" stroke-width="2.5"/>
  </svg>

  <address class="address address--church">3-9-4 Kawaranodai, Kaedeno-ku<br>Tokyo 162-0847 (Church)</address>
  <address class="address address--home">2-21 Ochibamachi, Kaedeno-ku<br>Tokyo 162-0893 (Home)</address>

  <div class="contact">
    <div class="contact__line">
      <svg class="contact__icon" viewBox="0 0 24 34" aria-hidden="true">
        <rect x="6" y="0" width="3" height="8" fill="var(--teal)"/>
        <rect x="2" y="7" width="20" height="27" rx="3" fill="var(--teal)"/>
        <rect x="6" y="11" width="12" height="7" fill="var(--turquoise)"/>
        <g fill="var(--turquoise)">
          <rect x="6" y="21" width="3" height="2"/><rect x="11" y="21" width="3" height="2"/><rect x="16" y="21" width="3" height="2"/>
          <rect x="6" y="25" width="3" height="2"/><rect x="11" y="25" width="3" height="2"/><rect x="16" y="25" width="3" height="2"/>
          <rect x="6" y="29" width="3" height="2"/><rect x="11" y="29" width="3" height="2"/><rect x="16" y="29" width="3" height="2"/>
        </g>
      </svg>
      <span>03-5817-2963</span>
    </div>
    <div class="contact__line">
      <svg class="contact__icon contact__icon--at" viewBox="0 0 30 30" aria-hidden="true">
        <circle cx="15" cy="15" r="15" fill="var(--teal)"/>
        <circle cx="15" cy="15" r="4.5" fill="none" stroke="var(--turquoise)" stroke-width="2.2"/>
        <path d="M19.5 12 V17 a2.5 2.5 0 0 0 5 0 V15 a9.5 9.5 0 1 0 -4 7.8" fill="none" stroke="var(--turquoise)" stroke-width="2.2"/>
      </svg>
      <span>pastor@maplegrovefell.org</span>
    </div>
    <div class="contact__line">
      <span>http://www.maplegrovefell.org</span>
    </div>
  </div>
</div>
</body>
</html>
```